Kestrel Valley Alpine Riders Society needs a business card design

We need a business card design for our newly incorporated KVARS. We are helping the NZ Chinese community, as well as everyone else, to organise ski & snowboarding trips, training, and equipments. The design should be creative, energetic, young and vibrant.

Industry/Entity Type

Social Club

Contact Information for Business Card

Logo; Kestrel Valley Alpine Riders Society; Name: Oliver Brandt; Position: President; Address: 42 Marwick Rd, Epsom, Auckland 1051; Mobile: 020 7826 1957; Email: oliver@kvars-club.example; Web: www.kvars-club.example

Requirements
Must have
• 1, The text "Kestrel Valley Alpine Riders Society" should be put together with the supplied logo file to form a new complete logo combination.
• 2, Final design files should be in Adobe Illustrator format and all text must be editable.
Nice to have
• two or three colours

```html
<!DOCTYPE html>
<html lang="en">
<head>
<meta charset="utf-8">
<title>Kestrel Valley Alpine Riders Society – Business Card</title>
<link rel="stylesheet" href="https://fonts.googleapis.com/css2?family=Ubuntu:wght@400;500;700&display=swap">
<style>
  :root {
    --backdrop: #e6e8eb;
    --sky-light: #3dc0ec;
    --sky-mid: #1fa7e0;
    --ice: #b9e6f8;
    --deep-blue: #1f63b8;
    --navy: #223f8e;
    --ink-navy: #1b2a66;
    --white: #ffffff;
    --shadow: rgba(20, 30, 60, 0.18);
  }
  * { box-sizing: border-box; margin: 0; padding: 0; }
  html, body {
    width: 1200px; height: 1006px; overflow: hidden;
    background: var(--backdrop);
    font-family: "Ubuntu", sans-serif;
  }
  .canvas { position: relative; width: 1200px; height: 1006px; }

  .card {
    position: absolute;
    width: 640px; height: 366px;
    border-radius: 4px;
    overflow: hidden;
    box-shadow: 0 12px 30px var(--shadow);
  }

  /* Front */
  .card-front {
    left: 90px; top: 80px;
    background: linear-gradient(180deg, var(--sky-light) 0%, var(--sky-mid) 55%, var(--ice) 100%);
  }
  .card-front .org-name {
    position: absolute; left: 34px; top: 30px;
    font-size: 26px; font-weight: 500; color: var(--navy);
  }
  .card-front .brand {
    position: absolute; left: 0; right: 0; top: 130px;
    display: flex; align-items: center; justify-content: center; gap: 16px;
  }
  .card-front .brand-dot {
    width: 26px; height: 26px; border-radius: 50%; background: var(--navy);
  }
  .card-front .brand-name {
    font-size: 92px; font-weight: 700; color: var(--navy); letter-spacing: 2px;
  }
  .card-front .rider-art {
    position: absolute; left: 110px; top: 240px; width: 150px; height: 110px;
    border-radius: 8px;
    background: radial-gradient(ellipse at center, rgba(34,63,142,0.45), rgba(34,63,142,0) 70%);
  }
  .card-front .snow-slope {
    position: absolute; left: 0; right: 0; bottom: 0; height: 90px;
    background: linear-gradient(180deg, rgba(255,255,255,0) 0%, rgba(230,246,253,0.85) 100%);
  }

  /* Back */
  .card-back {
    left: 470px; top: 540px;
    background: linear-gradient(180deg, var(--sky-mid) 0%, var(--deep-blue) 70%, var(--navy) 100%);
  }
  .card-back .org-name {
    position: absolute; left: 36px; top: 26px;
    font-size: 19px; font-weight: 500; color: var(--navy);
  }
  .card-back .brand {
    position: absolute; left: 36px; top: 66px;
    display: flex; align-items: center; gap: 8px;
  }
  .card-back .brand-dot {
    width: 12px; height: 12px; border-radius: 50%; background: var(--navy);
  }
  .card-back .brand-name {
    font-size: 40px; font-weight: 700; color: var(--navy);
  }
  .card-back .person {
    position: absolute; right: 54px; top: 108px; text-align: left;
  }
  .card-back .person-name {
    font-size: 30px; font-weight: 700; color: var(--white); line-height: 1.05;
  }
  .card-back .person-role {
    font-size: 23px; font-weight: 500; color: var(--ink-navy); letter-spacing: 1.5px;
  }
  .card-back .contact-list {
    position: absolute; left: 36px; top: 168px; list-style: none;
  }
  .card-back .contact-item {
    display: flex; align-items: center; height: 44px;
    font-size: 14px; color: var(--white);
  }
  .card-back .contact-item svg {
    width: 20px; height: 20px; margin-right: 28px; flex: none;
  }
  .card-back .rider-watermark {
    position: absolute; right: 60px; top: 190px; width: 200px; height: 150px;
    background: radial-gradient(ellipse at center, rgba(120,190,240,0.35), rgba(120,190,240,0) 70%);
  }
  .icon-stroke { fill: none; stroke: var(--sky-light); stroke-width: 1.6; }
  .icon-fill { fill: var(--sky-light); }
</style>
</head>
<body>
<main class="canvas">

  <section class="card card-front">
    <p class="org-name">Kestrel Valley Alpine Riders Society</p>
    <div class="brand">
      <span class="brand-dot"></span>
      <span class="brand-name">KVARS</span>
    </div>
    <div class="snow-slope"></div>
    <div class="rider-art" role="img" aria-label="Silhouette of a snowboarder jumping over a snowy slope"></div>
  </section>

  <section class="card card-back">
    <p class="org-name">Kestrel Valley Alpine Riders Society</p>
    <div class="brand">
      <span class="brand-name">KVARS</span>
      <span class="brand-dot"></span>
    </div>
    <div class="rider-watermark" role="img" aria-label="Faint snowboarder silhouette in the background"></div>
    <div class="person">
      <p class="person-name">Oliver Brandt</p>
      <p class="person-role">President</p>
    </div>
    <ul class="contact-list">
      <li class="contact-item">
        <svg viewBox="0 0 20 20" aria-hidden="true"><rect class="icon-stroke" x="5.5" y="1.5" width="9" height="17" rx="1.5"/><line class="icon-stroke" x1="8.5" y1="16" x2="11.5" y2="16"/></svg>
        020 7826 1957
      </li>
      <li class="contact-item">
        <svg viewBox="0 0 20 20" aria-hidden="true"><rect class="icon-stroke" x="1.5" y="4.5" width="17" height="11"/><polyline class="icon-stroke" points="1.5,4.5 10,11 18.5,4.5"/></svg>
        oliver@kvars-club.example
      </li>
      <li class="contact-item">
        <svg viewBox="0 0 20 20" aria-hidden="true"><circle class="icon-stroke" cx="10" cy="10" r="8"/><ellipse class="icon-stroke" cx="10" cy="10" rx="3.5" ry="8"/><line class="icon-stroke" x1="2" y1="10" x2="18" y2="10"/></svg>
        www.kvars-club.example
      </li>
      <li class="contact-item">
        <svg viewBox="0 0 20 20" aria-hidden="true"><path class="icon-fill" d="M10 1.5a6 6 0 0 0-6 6c0 4.5 6 11 6 11s6-6.5 6-11a6 6 0 0 0-6-6zm0 8.3a2.3 2.3 0 1 1 0-4.6 2.3 2.3 0 0 1 0 4.6z"/></svg>
        42 Marwick Rd, Epsom, Auckland 1051
      </li>
    </ul>
  </section>

</main>
</body>
</html>
```